Real Estate Savvy Investors looking to expand and fuel homeownership possibilities.

My company is called Tavmoor Holdings, LLC. My team specializes in residential and commercial real estate. We buy, sell and rent, FAST! We buy houses in any situation and condition, including Pre-Foreclosures and vacant homes. We trade homes and We provide creative financing, such as our lease to own option, in which we accept goods such as cars, boats etc., to go towards the purchase price of the home. In commercial real estate, we buy in any area and we are open to creative financing.

Target Market(s)

Preforeclosure homes, vacant homes, distressed homes, all home owners

Industry/Entity Type

Real Estate

Contact Information for Business Card

Should include company name (Tavmoor Holdings, LLC), company email TavmoorHoldingsLLC@quenmail.com, office phone 405-738-2914, P.O. Box 58037, ok, ok 73982)

Font styles to use
Serif

Colors

Designer to choose colors to be used in the design.

Requirements
Must have
• Must include what we specialize in: preforeclosures, vacant homes, distressed homes-any situation and condition.
• Somewhere on the card please include: Investment opportunities: 8%-10% return.

```html
<!DOCTYPE html>
<html lang="en">
<head>
<meta charset="utf-8">
<title>Tavmoor Holdings, LLC — Business Cards</title>
<link rel="stylesheet" href="https://fonts.googleapis.com/css2?family=Playfair+Display:wght@900&family=Source+Serif+4:wght@400;600&display=swap">
<style>
  :root {
    --page: #ffffff;
    --card-dark: #333333;
    --card-light: #ffffff;
    --rule-dark: #6a6a6a;
    --rule-light: #6e6e6e;
    --ink-dark: #bdbdbd;
    --ink-light: #111111;
    --name-dark: #b4b4b4;
    --name-light: #000000;
    --card-shadow: rgba(0, 0, 0, 0.45);
  }
  html, body {
    margin: 0;
    padding: 0;
    width: 1200px;
    height: 853px;
    overflow: hidden;
    background: var(--page);
  }
  .sheet {
    position: relative;
    width: 1200px;
    height: 853px;
  }
  .card {
    position: absolute;
    width: 365px;
    height: 203px;
    box-shadow: 3px 3px 4px var(--card-shadow);
    font-family: "Source Serif 4", Georgia, serif;
  }
  .card--dark { background: var(--card-dark); color: var(--ink-dark); }
  .card--light { background: var(--card-light); color: var(--ink-light); }
  .card--dark .card__text { text-shadow: 1px 1px 1px rgba(0,0,0,0.8); }
  .card--light .card__text { text-shadow: 1px 1px 1px rgba(0,0,0,0.2); }

  .card--front-dark { left: 204px; top: 218px; }
  .card--back-dark  { left: 635px; top: 218px; }
  .card--front-light { left: 204px; top: 483px; }
  .card--back-light  { left: 635px; top: 483px; }

  .card__name {
    position: absolute;
    left: 0; right: 0;
    top: 22px;
    margin: 0;
    text-align: center;
    font-family: "Playfair Display", Georgia, serif;
    font-weight: 900;
    font-size: 27px;
    line-height: 30px;
    letter-spacing: -0.3px;
    white-space: nowrap;
  }
  .card--dark .card__name { color: var(--name-dark); text-shadow: 2px 2px 1px rgba(0,0,0,0.85); }
  .card--light .card__name { color: var(--name-light); }
  .card__name-suffix { font-size: 19px; letter-spacing: 0; }

  .card__rule {
    position: absolute;
    left: 0; right: 0;
    height: 1px;
  }
  .card--dark .card__rule { background: var(--rule-dark); }
  .card--light .card__rule { background: var(--rule-light); }
  .card__rule--top { top: 73px; }
  .card__rule--bottom { top: 179px; }

  .card__line {
    position: absolute;
    left: 0; right: 0;
    margin: 0;
    text-align: center;
    line-height: 1;
    white-space: nowrap;
  }
  .card__email { top: 84px; font-size: 15px; }
  .card__phone { top: 106px; font-size: 21px; }
  .card__street { top: 135px; font-size: 15px; }
  .card__city { top: 155px; font-size: 15px; }
  .card__invest { top: 185px; font-size: 11.5px; font-weight: 600; letter-spacing: 0.3px; }

  .specialties {
    position: absolute;
    left: 26px;
    top: 0;
    margin: 0;
    padding: 0;
    list-style: none;
  }
  .specialties__item {
    position: absolute;
    left: 0;
    white-space: nowrap;
    font-size: 19px;
    line-height: 1;
  }
  .specialties__item::before {
    content: "";
    display: inline-block;
    width: 7px; height: 7px;
    border-radius: 50%;
    background: currentColor;
    margin-right: 8px;
    vertical-align: 3px;
  }
  .specialties__item:nth-child(1) { top: 87px; }
  .specialties__item:nth-child(2) { top: 119px; }
  .specialties__item:nth-child(3) { top: 149px; }
</style>
</head>
<body>
<main class="sheet">

  <section class="card card--dark card--front-dark">
    <h1 class="card__name">Tavmoor Holdings,<span class="card__name-suffix">LLC</span></h1>
    <div class="card__rule card__rule--top"></div>
    <p class="card__line card__text card__email">TavmoorHoldingsLLC@quenmail.com</p>
    <p class="card__line card__text card__phone">405-738-2914</p>
    <p class="card__line card__text card__street">P.O. Box 58037</p>
    <p class="card__line card__text card__city">ok 73982</p>
    <div class="card__rule card__rule--bottom"></div>
    <p class="card__line card__text card__invest">Investment opportunities: 8%-10% return</p>
  </section>

  <section class="card card--dark card--back-dark">
    <h2 class="card__name">Tavmoor Holdings,<span class="card__name-suffix">LLC</span></h2>
    <div class="card__rule card__rule--top"></div>
    <ul class="specialties">
      <li class="specialties__item card__text">preforeclosures</li>
      <li class="specialties__item card__text">vacant homes</li>
      <li class="specialties__item card__text">distressed homes</li>
    </ul>
    <div class="card__rule card__rule--bottom"></div>
    <p class="card__line card__text card__invest">Investment opportunities: 8%-10% return</p>
  </section>

  <section class="card card--light card--front-light">
    <h2 class="card__name">Tavmoor Holdings,<span class="card__name-suffix">LLC</span></h2>
    <div class="card__rule card__rule--top"></div>
    <p class="card__line card__text card__email">TavmoorHoldingsLLC@quenmail.com</p>
    <p class="card__line card__text card__phone">405-738-2914</p>
    <p class="card__line card__text card__street">P.O. Box 58037</p>
    <p class="card__line card__text card__city">ok 73982</p>
    <div class="card__rule card__rule--bottom"></div>
    <p class="card__line card__text card__invest">Investment opportunities: 8%-10% return</p>
  </section>

  <section class="card card--light card--back-light">
    <h2 class="card__name">Tavmoor Holdings,<span class="card__name-suffix">LLC</span></h2>
    <div class="card__rule card__rule--top"></div>
    <ul class="specialties">
      <li class="specialties__item card__text">preforeclosures</li>
      <li class="specialties__item card__text">vacant homes</li>
      <li class="specialties__item card__text">distressed homes</li>
    </ul>
    <div class="card__rule card__rule--bottom"></div>
    <p class="card__line card__text card__invest">Investment opportunities: 8%-10% return</p>
  </section>

</main>
</body>
</html>
```